Swim school needs flyer design

Need revamp of flyer design. Attached last years flyer (RTC A4 Holiday Leaflet-v6.2 (1)). Also attached is this years information in word format (RTC A4 RTC & Holiday Leaflet 2014-2015).
This flyer must fit with our logo (Ripple Tide Club-RGB). This flyer is our first point of call for many of our clients. With the amount of information that must be provided, it is important that it flows and is appealing. Photos can be accessed from http://marlapics.fotonest.example/apps/photos/album?albumid=27391540 or from your own source
Important that the final design fits printers template.(Flyers-A4-210x297mm-2Side - attached)

```html
<!DOCTYPE html>
<html lang="en">
<head>
<meta charset="utf-8">
<title>Holiday Swim Classes – Ripple Tide Club</title>
<link rel="stylesheet" href="https://fonts.googleapis.com/css2?family=Arimo:ital,wght@0,400;0,700;1,400&family=Delius&family=Roboto+Condensed:ital,wght@1,700&display=swap">
<style>
:root{
  --teal:#1fa3c9;
  --teal-dark:#0f7fa8;
  --orange:#f18a00;
  --orange-text:#f08c1a;
  --lime:#b7cc0a;
  --lime-light:#cfe04a;
  --ink:#111;
  --white:#fff;
  --water-top:#6ec6e6;
  --water-bottom:#d9f0f8;
}
*{margin:0;padding:0;box-sizing:border-box}
html,body{width:849px;height:1200px;overflow:hidden;background:var(--white)}
.flyer{position:relative;width:849px;height:1200px;overflow:hidden;background:var(--white);font-family:"Arimo",Arial,sans-serif;color:var(--ink)}
.abs{position:absolute}
.hero-photo{left:0;top:0;width:849px;height:350px;background:linear-gradient(180deg,var(--water-top),#a7dcef 60%,var(--water-bottom))}
.clouds{left:0;top:230px}
.title-bubble{left:16px;top:12px;width:182px;height:134px}
.title-bubble span{position:absolute;left:34px;top:14px;font-family:"Delius",cursive;color:var(--white);font-size:32px;line-height:29px}
.brand-box{left:549px;top:17px;width:300px;height:163px;background:var(--white);border-radius:18px 0 0 18px;display:flex;align-items:center;justify-content:center;gap:10px}
.brand-box .dot{width:18px;height:18px;border-radius:50%;background:var(--orange)}
.brand-name{font-family:"Arimo",sans-serif;font-weight:700;font-size:29px;color:var(--teal)}
.phone-pill{left:24px;top:226px;width:184px;height:70px}
.phone-pill .num{position:absolute;left:32px;top:16px;font-family:"Roboto Condensed",sans-serif;font-style:italic;font-weight:700;font-size:33px;color:var(--white)}
.web{left:24px;top:300px;font-size:13px;font-weight:700;color:var(--teal-dark)}
.important{left:535px;top:262px;width:300px}
.important h2{font-family:"Delius",cursive;font-weight:400;font-size:27px;color:var(--orange);margin-left:96px;margin-bottom:6px}
.important ul{list-style:none}
.important li{position:relative;padding-left:16px;font-size:13px;font-weight:700;color:var(--teal);line-height:17px;margin-bottom:10px}
.important li::before{content:"★";position:absolute;left:0;top:0;color:var(--lime);font-size:11px}
.pool-info{left:19px;top:356px}
.pool-info h2{font-family:"Delius",cursive;font-weight:400;font-size:34px;color:var(--orange);line-height:42px}
.pool-info .detail{font-family:"Delius",cursive;font-size:21px;color:var(--orange);line-height:27px}
.pool-info .note{font-size:13px;font-weight:700;line-height:17px;margin-top:6px}
.pool-info .places{font-size:13px;margin-top:8px;margin-left:2px}
.inset-photo{left:272px;top:322px;width:258px;height:178px}
.banner{left:33px;top:542px;width:774px;height:103px;background:var(--lime);border:3px solid var(--teal);border-radius:26px 26px 26px 26px / 20px 20px 40px 40px;font-family:"Delius",cursive;font-size:21px;line-height:26px;text-align:center;padding:12px 30px 0}
.wave-band{left:0;top:985px;width:849px;height:215px;background:linear-gradient(180deg,#dff2f8 0%,var(--lime-light) 45%,var(--orange) 100%)}
.contact{left:17px;top:665px;width:456px;height:512px;background:var(--white);border:1.5px solid var(--teal);border-radius:10px;padding:12px 16px}
.contact h2{font-size:25px;color:var(--orange-text);line-height:34px;font-weight:700}
.contact h3{font-size:18px;font-weight:700;margin-top:18px;margin-bottom:10px}
.contact h3.orange{color:var(--orange-text);margin-top:26px}
.contact h3.blue{color:var(--teal)}
.row{display:flex;font-size:16px;line-height:20px;margin:0 0 12px 37px}
.row .label{white-space:nowrap}
.row .val{color:var(--orange-text);margin-left:4px}
.contact .row .val.blue{color:var(--teal)}
.hours{display:grid;grid-template-columns:120px auto;color:var(--orange-text)}
.dates{left:491px;top:665px;width:333px;height:510px;background:var(--orange)}
.dates .frame{position:absolute;left:6px;top:6px;right:6px;bottom:6px;border:2px dotted var(--white)}
.dates h2{position:absolute;left:16px;top:22px;font-family:"Delius",cursive;font-weight:400;font-size:27px;color:var(--white)}
.ribbon{position:absolute;height:53px;background:var(--lime);font-family:"Delius",cursive;font-size:36px;color:var(--white);line-height:53px}
.ribbon.y2014{left:-6px;top:64px;width:246px;clip-path:polygon(0 0,100% 0,88% 100%,0 100%);padding-left:50px}
.ribbon.y2015{left:96px;top:210px;width:243px;clip-path:polygon(0 0,100% 0,100% 100%,10% 100%);padding-left:74px}
.date-list{position:absolute;left:40px;list-style:none}
.date-list li{font-size:22px;font-weight:700;color:var(--white);line-height:32px;position:relative;padding-left:14px}
.date-list li::before{content:"★";position:absolute;left:-2px;top:1px;font-size:12px;color:#8a5a20}
.list-2014{top:130px}
.list-2015{top:270px}
.footnote{position:absolute;left:24px;top:473px;font-style:italic;font-size:18px;color:var(--ink)}
</style>
</head>
<body>
<div class="flyer">
  <div class="abs hero-photo" role="img" aria-label="Photo of a young child in a blue cap and goggles swimming underwater in a bright blue pool"></div>

  <svg class="abs clouds" width="849" height="140" viewBox="0 0 849 140" aria-hidden="true">
    <path fill="#fff" d="M0 110 C40 95 80 100 120 108 C170 92 230 95 280 110 C330 100 350 112 390 118 L400 140 L0 140 Z"/>
    <path fill="#fff" d="M540 60 C560 30 600 25 620 45 C640 20 700 18 720 40 C740 20 800 22 820 40 C835 35 849 38 849 40 L849 140 L380 140 C400 110 460 100 500 105 C505 85 520 70 540 60 Z"/>
  </svg>

  <svg class="abs title-bubble" viewBox="0 0 182 134" aria-hidden="true">
    <defs><radialGradient id="bubbleFill" cx="40%" cy="35%" r="70%"><stop offset="0" stop-color="#3fc0ea"/><stop offset="1" stop-color="#0a86c4"/></radialGradient></defs>
    <path fill="url(#bubbleFill)" stroke="#fff" stroke-width="2" d="M91 3 C150 3 180 30 180 62 C180 95 150 115 110 118 C90 120 70 132 60 133 C64 125 62 118 55 115 C20 108 2 90 2 62 C2 28 35 3 91 3 Z"/>
    <text></text>
  </svg>
  <div class="abs title-bubble" style="pointer-events:none"><span>Holiday<br>&nbsp;Swim<br>&nbsp;&nbsp;Classes</span></div>

  <div class="abs brand-box"><span class="dot"></span><span class="brand-name">Ripple Tide Club</span></div>

  <svg class="abs phone-pill" viewBox="0 0 184 70" aria-hidden="true">
    <path fill="#f7931e" stroke="#fbb040" stroke-width="2" d="M20 12 C70 2 150 0 176 10 C186 30 178 55 160 60 C110 68 50 68 14 62 C4 45 6 24 20 12 Z"/>
    <path fill="#1a8fc0" d="M12 24 C8 20 14 14 18 18 L22 24 C24 28 20 30 18 32 C20 38 24 42 28 46 C30 44 34 42 36 46 L38 52 C38 56 32 58 28 56 C16 50 10 38 12 24 Z"/>
  </svg>
  <div class="abs phone-pill"><span class="num">9380 2741</span></div>
  <div class="abs web">www.rippletideclub.example</div>

  <section class="abs important">
    <h2>Important</h2>
    <ul>
      <li>All holiday swim classes are conducted at the Fernbrook primary school pool</li>
      <li>30 minute classes run every ½ hour from 9.30am to 12 noon</li>
      <li>Limited places due to small class sizes</li>
      <li>Beginners to advanced swimmers welcome</li>
      <li>All children are grouped by age and ability</li>
      <li>No refunds or makeups for holiday programs</li>
    </ul>
  </section>

  <section class="abs pool-info">
    <h2>Salt Water Pool</h2>
    <p class="detail">Ages 3 and older</p>
    <p class="detail">$75 per child per week</p>
    <p class="detail">(5x½ hour classes per week)</p>
    <p class="note">No bookings are taken without a fully<br>completed enrolment form and payment.</p>
    <p class="places">Places are limited so book early to avoid disappointment.</p>
  </section>

  <svg class="abs inset-photo" viewBox="0 0 258 178" role="img" aria-label="Photo of a child in goggles kicking with an orange float board in a pool">
    <defs><linearGradient id="insetWater" x1="0" y1="0" x2="1" y2="1"><stop offset="0" stop-color="#7fcbe6"/><stop offset="1" stop-color="#3aa7d3"/></linearGradient></defs>
    <path fill="url(#insetWater)" stroke="#8cc63f" stroke-width="6" d="M40 20 C90 0 200 2 240 30 C262 50 255 110 240 140 C220 172 120 178 60 165 C15 155 2 110 8 70 C12 45 22 28 40 20 Z"/>
    <path fill="none" stroke="#1fa3c9" stroke-width="3" d="M36 14 C90 -6 205 -4 246 26"/>
  </svg>

  <div class="abs banner">Our qualified staff makes learn to swim not only a rewarding but also a lot of fun. This is a great opportunity to kick-start your child’s aquatic education.</div>

  <div class="abs wave-band" role="img" aria-label="Decorative band of flowing blue, green and orange waves with dotted lines"></div>

  <section class="abs contact">
    <h2>Pool Locations Contact Details<br>&amp; Office Hours</h2>
    <h3 class="orange">Fernbrook P.S. Pool</h3>
    <div class="row"><span class="label">Address:</span><span class="val">42 Marlow Street, Fernbrook 3091</span></div>
    <div class="row"><span class="label">Phone:</span><span class="val">9380 2741</span></div>
    <div class="row"><span class="label">Office Hours:</span><span class="val hours"><span>Mon to Fri</span><span>9:00am-5.30pm</span><span>Sat and Sun</span><span>9.15am-12.15pm</span></span></div>
    <h3 class="blue">Westmere Grammar Pool</h3>
    <div class="row"><span class="label">Address:</span><span class="val blue">Gate 1, Linden Street, Westmere 3077</span></div>
    <h3 class="orange" style="margin-top:16px">All Correspondence</h3>
    <div class="row"><span class="label">Post:</span><span class="val">P.O. Box 4816, East Westmere 3078</span></div>
    <div class="row"><span class="label">Email:</span><span class="val">info@rippletideclub.example</span></div>
    <div class="row"><span class="label">ABN:</span><span class="val">61 208 337 594</span></div>
  </section>

  <section class="abs dates">
    <div class="frame"></div>
    <h2>Holiday Program Dates</h2>
    <div class="ribbon y2014">2014</div>
    <ul class="date-list list-2014">
      <li>Sep 23rd – 27th</li>
      <li>Sep 30th – Oct 4th</li>
    </ul>
    <div class="ribbon y2015">2015</div>
    <ul class="date-list list-2015">
      <li>Jan 6th – 10th</li>
      <li>Jan 13th – 17th</li>
      <li>Jan 20th – 24th</li>
      <li>Mar 30th – Apr 3rd</li>
      <li>Apr 6th – 10th</li>
      <li>Jun 29th – Jul 3rd</li>
    </ul>
    <p class="footnote">* $52 per child due to 4 day week</p>
  </section>
</div>
</body>
</html>
```